IT Services Business Card Design

We require a business card design for an IT services company called RT Code Transit.

We specialize in taking an organisations software and readying it for deployment to new environments (e.g. Nex 3 to Nex 5). This process is termed application packaging. This is not the same as putting things in boxes but I am happy to use boxes as a pun icon ;-) This is our second step in branding, we currently have a new logo and our poor excuse of a website is next to be updated but it contains information on who we are and what we cover at rtcodetransit.example

We are looking for a fun, modern but stylish and professional looking design.

I have attached the logo in multiple formats including vector formats (and the fonts that created the logo if required)
Updates

Thanks to all the designers so far, some great designs in there.  I will be selecting a card design on the deadline date. 

However, there is still time to submit some more designs.  The majority of the ones I have so far are typical simplistic designs that we have all seen before and I have enough of those to choose from now.  If you wish to submit any more designs, please submit somthing unusual to grab our attention.

Target Market(s)

Project executives of large organisations looking for Nexora migrations

Industry/Entity Type

Software

Requirements
Must have
• Want to show company name, contact name, title, main number, contact number, fax number, email address and website address. I do not want to show the address.
Must use the attached logo, retaining the colours in them.

This has to be a double-sided design. I will be using pelby.example and will be selecting their rounded corner business card design.

Their templates and design requirements (sizing etc.) can be found here: http://uk.pelby.example/help/faq/templates-and-guidelines.html

Happy for company name or website to be on either side of the card.

This design has to be original and not used before for another company

Would like to style it around the business colours in the logo
Nice to have
• Pelby.example has an option for multiple card designs to appear on the back. If this is possible in the budget and time you have and you have a design(s) that work with that but carry the same style and theme, that would be nice to see but not necessary.
Should not have
• We do not want to put a postal address on the cards

```html
<!DOCTYPE html>
<html lang="en">
<head>
<meta charset="utf-8">
<title>RT Code Transit Business Card</title>
<link href="https://fonts.googleapis.com/css2?family=Jost:wght@400;500&display=swap" rel="stylesheet">
<style>
  :root {
    --backdrop: #c9c9c9;
    --card-white: #f4f4f4;
    --card-grey: #dcdcdc;
    --card-dark: #222423;
    --brand-blue: #4f6fe0;
    --brand-blue-deep: #2336b8;
    --brand-blue-light: #7d95ee;
    --text-dark: #2b2b2b;
    --text-light: #f2f2f2;
    --text-grey: #6d6d6d;
  }
  * { box-sizing: border-box; margin: 0; padding: 0; }
  html, body { width: 1200px; height: 861px; overflow: hidden; }
  body {
    background: var(--backdrop);
    font-family: "Jost", "Futura", sans-serif;
    display: flex;
    flex-direction: column;
    align-items: center;
    justify-content: center;
    gap: 56px;
  }
  .card {
    position: relative;
    width: 620px;
    height: 360px;
    border-radius: 14px;
    overflow: hidden;
    box-shadow: 0 6px 18px rgba(0,0,0,0.18);
  }
  .card-art { position: absolute; inset: 0; width: 100%; height: 100%; }
  .brand {
    position: absolute;
    top: 30px;
    right: 30px;
    display: flex;
    flex-direction: column;
    align-items: flex-end;
    gap: 10px;
  }
  .brand-name {
    font-size: 26px;
    font-weight: 400;
    line-height: 1.05;
    letter-spacing: 0.5px;
    text-align: right;
  }
  .brand-dot {
    width: 30px; height: 30px; border-radius: 50%;
    background: var(--brand-blue);
  }
  .contact {
    position: absolute;
    left: 40px;
    top: 108px;
    list-style: none;
    font-size: 17px;
    line-height: 1;
  }
  .contact li { display: flex; align-items: center; gap: 10px; height: 28px; }
  .contact svg { width: 20px; height: 20px; flex: none; }
  .person { position: absolute; left: 40px; top: 262px; }
  .person-name {
    font-size: 30px; font-weight: 400; color: var(--brand-blue);
    letter-spacing: 1px; line-height: 1;
  }
  .person-title { font-size: 17px; color: var(--text-grey); margin-top: 4px; }

  .card--light { background: var(--card-white); }
  .card--light .brand-name { color: #9a9a9a; }
  .card--light .contact { color: var(--text-dark); }

  .card--dark { background: var(--card-dark); }
  .card--dark .brand-name { color: #4a4a4a; }
  .card--dark .contact { color: var(--text-light); }
  .card--dark .person-title { color: #d8d8d8; }
</style>
</head>
<body>

<svg width="0" height="0" style="position:absolute" aria-hidden="true">
  <defs>
    <linearGradient id="stripe-blue" x1="0" y1="0" x2="0" y2="1">
      <stop offset="0" stop-color="var(--brand-blue-light)"/>
      <stop offset="1" stop-color="var(--brand-blue-deep)"/>
    </linearGradient>
    <linearGradient id="paper-light" x1="0" y1="0" x2="1" y2="1">
      <stop offset="0" stop-color="var(--card-white)"/>
      <stop offset="1" stop-color="var(--card-grey)"/>
    </linearGradient>
    <symbol id="icon-phone" viewBox="0 0 20 20">
      <circle cx="10" cy="10" r="10" fill="var(--brand-blue)"/>
      <path d="M7 5c1 0 1.6 2 1.4 2.6l-1 .8c.5 1.4 1.7 2.7 3.2 3.3l.8-1c.6-.2 2.6.4 2.6 1.4 0 1-1 2-2 2C8.6 14.1 5.9 11.4 5 7c0-1 1-2 2-2z" fill="#fff"/>
    </symbol>
    <symbol id="icon-mobile" viewBox="0 0 20 20">
      <circle cx="10" cy="10" r="10" fill="var(--brand-blue)"/>
      <rect x="7" y="4.5" width="6" height="11" rx="1" fill="#fff"/>
      <rect x="8" y="6" width="4" height="6.5" fill="var(--brand-blue)"/>
    </symbol>
    <symbol id="icon-fax" viewBox="0 0 20 20">
      <circle cx="10" cy="10" r="10" fill="var(--brand-blue)"/>
      <rect x="7" y="4.5" width="6" height="4" fill="#fff"/>
      <rect x="5" y="8.5" width="10" height="6" rx="1" fill="#fff"/>
    </symbol>
    <symbol id="icon-mail" viewBox="0 0 20 20">
      <circle cx="10" cy="10" r="10" fill="var(--brand-blue)"/>
      <rect x="5" y="6.5" width="10" height="7" fill="#fff"/>
      <path d="M5 6.5l5 4 5-4" stroke="var(--brand-blue)" stroke-width="1" fill="none"/>
    </symbol>
    <symbol id="icon-web" viewBox="0 0 20 20">
      <circle cx="10" cy="10" r="10" fill="var(--brand-blue)"/>
      <circle cx="10" cy="10" r="5" fill="none" stroke="#fff" stroke-width="1.2"/>
      <path d="M5 10h10M10 5v10M6.5 7h7M6.5 13h7" stroke="#fff" stroke-width="1"/>
    </symbol>
  </defs>
</svg>

<section class="card card--light" aria-label="Business card, light side">
  <svg class="card-art" viewBox="0 0 620 360" aria-hidden="true">
    <rect width="620" height="360" fill="url(#paper-light)"/>
    <path d="M350 0H620V360H500C460 240 415 110 350 0Z" fill="var(--card-dark)"/>
    <path d="M362 0C425 110 470 240 508 360H548C505 240 452 110 392 0Z" fill="url(#stripe-blue)"/>
    <path d="M402 0C462 110 515 240 558 360H572C528 240 474 110 414 0Z" fill="url(#stripe-blue)"/>
  </svg>
  <div class="brand"><p class="brand-name">RT Code<br>Transit</p><span class="brand-dot"></span></div>
  <ul class="contact">
    <li><svg><use href="#icon-phone"/></svg>123 456 7890</li>
    <li><svg><use href="#icon-mobile"/></svg>123 567 8901</li>
    <li><svg><use href="#icon-fax"/></svg>123 678 9012</li>
    <li><svg><use href="#icon-mail"/></svg>name@rtcodetransit.example</li>
    <li><svg><use href="#icon-web"/></svg>www.rtcodetransit.example</li>
  </ul>
  <div class="person">
    <p class="person-name">NAME SURNAME</p>
    <p class="person-title">Title</p>
  </div>
</section>

<section class="card card--dark" aria-label="Business card, dark side">
  <svg class="card-art" viewBox="0 0 620 360" aria-hidden="true">
    <rect width="620" height="360" fill="var(--card-dark)"/>
    <path d="M350 0H620V360H480C445 240 405 110 350 0Z" fill="url(#paper-light)"/>
    <path d="M366 0C420 110 462 240 492 360H530C495 240 450 110 396 0Z" fill="url(#stripe-blue)"/>
    <path d="M404 0C456 110 500 240 538 360H552C516 240 470 110 416 0Z" fill="url(#stripe-blue)"/>
  </svg>
  <div class="brand"><p class="brand-name">RT Code<br>Transit</p><span class="brand-dot"></span></div>
  <ul class="contact">
    <li><svg><use href="#icon-phone"/></svg>123 456 7890</li>
    <li><svg><use href="#icon-mobile"/></svg>123 567 8901</li>
    <li><svg><use href="#icon-fax"/></svg>123 678 9012</li>
    <li><svg><use href="#icon-mail"/></svg>name@rtcodetransit.example</li>
    <li><svg><use href="#icon-web"/></svg>www.rtcodetransit.example</li>
  </ul>
  <div class="person">
    <p class="person-name">NAME SURNAME</p>
    <p class="person-title">Title</p>
  </div>
</section>

</body>
</html>
```